Business Card for Managing Partner Investment Fund

To create a business card template for an investment fund manager. Business card should be more professional in nature, not too colorful, more upscale, and created using the attached logos and fund name files. I would prefer a black or gray color scheme, but am open to the use of color as well. I would prefer a double sided business card, but open to single sided business card designs as well. The business card should include: name, title, and contact information, as well as logo and company name. I would prefer a more stream-lined, simple business card design.
Updates
Address: 4190 NE 38th Ter. Ocala, FL 34470
Email: talvin47@quorimail.net
Phone: 561-347-9162
Title: managing partner
Name: Dorian Velsky
Fund Name: Ambergate Capital
Logos can be found in files attached to the brief
Target Market(s)
potential investors, other fund managers
Industry/Entity Type
Finance
Contact Information for Business Card
Name on card: Dorian Velsky
Title: Managing Partner
Colors
Designer to choose colors to be used in the design.
Requirements
Must have
- Phone number
- email address
- physical address
- title
- name
- logo
- Fund name
Nice to have
- simple layout
Should not have
- too many colors, busy fonts,

```html
<!DOCTYPE html>
<html lang="en">
<head>
<meta charset="utf-8">
<title>Ambergate Capital – Business Card</title>
<link rel="stylesheet" href="https://fonts.googleapis.com/css2?family=Lato:wght@300;400&family=Josefin+Sans:wght@700&display=swap">
<style>
  :root {
    --brand-blue: #3767b1;
    --ink: #222222;
    --paper: #ffffff;
    --frame: #222222;
  }
  * { box-sizing: border-box; margin: 0; padding: 0; }
  html, body { width: 1200px; height: 1000px; overflow: hidden; background: var(--paper); }
  .canvas { position: relative; width: 1200px; height: 1000px; }

  .card {
    position: absolute;
    left: 273px;
    width: 644px;
    height: 369px;
    border: 3px solid var(--frame);
    overflow: hidden;
  }
  .card--front { top: 97px; background: var(--paper); }
  .card--back { top: 536px; background: var(--brand-blue); }

  .front-panel { position: absolute; inset: 0; width: 100%; height: 100%; }

  .holder { position: absolute; left: 44px; top: 42px; color: var(--ink); }
  .holder__name {
    font-family: "Josefin Sans", sans-serif;
    font-weight: 700;
    font-size: 27px;
    font-variant: small-caps;
    line-height: 1.1;
  }
  .holder__title {
    font-family: "Lato", sans-serif;
    font-weight: 400;
    font-size: 18px;
    margin-top: 2px;
  }

  .contact { position: absolute; left: 43px; top: 124px; list-style: none; }
  .contact__item {
    display: flex;
    align-items: center;
    height: 32px;
    margin-bottom: 11px;
    font-family: "Lato", sans-serif;
    font-weight: 300;
    font-size: 19px;
    color: var(--ink);
  }
  .contact__key {
    width: 32px; height: 30px;
    border: 2.5px solid var(--ink);
    display: flex; align-items: center; justify-content: center;
    font-weight: 400;
    font-size: 18px;
    margin-right: 19px;
  }

  .brand-name {
    position: absolute;
    color: var(--paper);
    font-family: "Lato", sans-serif;
    font-weight: 400;
    text-align: center;
    line-height: 1.15;
  }
  .brand-name--front { left: 380px; top: 262px; width: 240px; font-size: 26px; }
  .brand-name--back { left: 0; right: 0; top: 210px; font-size: 52px; }
</style>
</head>
<body>
<main class="canvas">
  <section class="card card--front" aria-label="Card front">
    <svg class="front-panel" viewBox="0 0 638 363" preserveAspectRatio="none" aria-hidden="true">
      <path fill="#3767b1" d="M470 0 Q430 220 236 363 L638 363 L638 0 Z"/>
    </svg>
    <div class="holder">
      <h1 class="holder__name">Dorian Velsky</h1>
      <p class="holder__title">Managing Partner</p>
    </div>
    <ul class="contact">
      <li class="contact__item"><span class="contact__key">A</span>4190 NE 38th Ter. Ocala, FL 34470</li>
      <li class="contact__item"><span class="contact__key">P</span>561-347-9162</li>
      <li class="contact__item"><span class="contact__key">E</span>talvin47@quorimail.net</li>
    </ul>
    <p class="brand-name brand-name--front">Ambergate Capital</p>
  </section>

  <section class="card card--back" aria-label="Card back">
    <p class="brand-name brand-name--back">Ambergate Capital</p>
  </section>
</main>
</body>
</html>
```